Sitecraft website build: Quirk literary annual (initial design work supplied)

Our brand guidelines provide the look and feel for the website - we just need someone to create it based on our mock ups!
PLEASE NOTE:
- Please base our website off the website pages within the brief (ie homepage is GREEN)
- please ensure each page will be standalone (not a scrolling home page)
- please only use filtered duotone style photography as a hold, if you think the page needs a photo.
-please not the websites i have provided as an influence - especially TIDE YEARLY. We want very little photography.

Quirk is a literary and arts journal that provides a platform for both emerging and established writers and artists from New Zealand and beyond. We are passionate about sharing insights into the intimate and unique worlds of creatives with short stories, poetry, and art – showcasing raw and unfiltered glimpses into their world.

We have our brand guidelines and logo finalised, with a 'look and feel' design for the website within our attached brand guidelines document. We just need someone to design this simple website on Sitecraft for us. It will have five pages and will need a newsletter sign up link:
Home page
About us page
Submissions page
Purchase page
Contact page

DRAFT WEB COPY

ABOUT
QUIRK is an independent literary annual journal established in 2022 by Hazel Wintergate and Mereana Clift that publishes unrepentant unfiltered accounts of life, eclectic takes on the mundane ordinary, and deep dives into modern love & sexuality.
Founder, Editor: Hazel Arohanui Wintergate
Founder, Production Director: Mereana Clift
Art Direction: Lorna Pike
Editorial Assistant: Kirsten Holloway-Dunn

I suggest duotone fashion-esque photography which is very Vesna Kordell/ Palm Springs vibe but not obviously identifiable.
· I love the style of Rufus Tennick for our shoot in particular. Group lazing around a pool, leisurely, glam, but effortless and ironically looking very natural – as though – yes, these are our lives.
SUBMISSION PAGE
Quirk welcomes submissions all year round.
We are drawn to dark humour, satirical takes on the social scene, and starkly honest accounts of ordinary life. Diversity is celebrated, adversity is welcomed and, above all, personal expression is championed. We are particularly seeking content that takes risks, screams of honesty and celebrates life’s most extraordinary moments.
Selected works will be published in our annual publication.

Submission guidelines
We accept flash fiction, short stories and poetry. Individual entries not to mustn’t exceed 2000 words.
Submitted work must be unpublished and in English. We welcome simultaneous submissions, but must be notified immediately if your manuscript is accepted for publication elsewhere or appears in any print or online source. We will endeavour to respond to all submissions within four weeks.
Please send submissions as a word document along with a brief bio of 50 words to pages@quirkjournal.test
PO Box[EB2]
​Note on Copyright: Copyright remains with the author.

Annual short story competition
Volume Alpha is interested in all that is spiritual, coincidental, or mysterious. Stories selected for this issue reflect life’s uncanny moments, those that defy explanation, and experiences that promote personal and spiritual growth. Entires must be no longer than 2000 words.

First prize: 1000
Second prize: 500
Third prize: 200[EB3]

SUPPORT US
Since our launch in 2022, we have relied upon the generous support of our creative business community in Wellington City, New Zealand. If you read us, or love our ethos, please consider a donation.
Link to chipinhere page
Updates

Hello designers
I would ideally love to have someone turn this around within a few weeks, because the design work has mostly been provided.
Thanks
Hazel

Hi everyone Please ensure you read our brand guidelines and follow the brief. Please note we do not yet have a product, as this is a new venture, so there is no point including images of a magazine that doesn't yet exist. Some further comment to ensure we get there: - We want all pages to be separate pages (not a scrolling home page) with a different colour based on the guidelines - The home page must look just as it does in the brand guidelines - There is no archive page (please read brief) as we have no archive yet. The pages are: Home, About, Contact, Competitions and submissions Thank you

Target Market(s)

writers and creatives

Industry/Entity Type

Writing/ creative/ publishing

Coding

Coded - Design and coding required

Number of Pages Required

4 page

Font styles to use
Other font styles liked:
• COTTA and Univers - as per brand guidelines

Requirements
Must have
• Sitecraft designer needed to design our mocked up webpages.
Nice to have
• As close to the brand guideline mock ups as possible (see page 11,12,13)
Should not have
• anything outside of the brand guidelines

```html
<!DOCTYPE html>
<html lang="en">
<head>
<meta charset="utf-8">
<title>Quirk — literary and arts journal</title>
<link href="https://fonts.googleapis.com/css2?family=Cormorant+Garamond:wght@300;400;500&family=Jost:wght@300;400;500&family=Oswald:wght@300;400&display=swap" rel="stylesheet">
<style>
:root{
  --plum:#6d3c62;
  --plum-deep:#5a2a50;
  --gold:#b79a2b;
  --ink:#1f1a1e;
  --grey:#6f6670;
  --lavender:#e6d6ef;
  --white:#ffffff;
  --cream:#f3ebdc;
  --olive:#6b7a2a;
  --rose:#c4587a;
}
*{margin:0;padding:0;box-sizing:border-box}
html,body{width:1200px;height:3745px;overflow:hidden}
body{position:relative;background:var(--white);font-family:"Jost",sans-serif;color:var(--ink)}
.abs{position:absolute}
.serif{font-family:"Cormorant Garamond",serif;font-weight:400}
.cond{font-family:"Oswald",sans-serif;font-weight:300;text-transform:uppercase}

/* hero */
.hero{position:absolute;left:0;top:0;width:1200px;height:721px;background:var(--plum);color:var(--white)}
.nav-link{position:absolute;top:70px;font-size:18px;letter-spacing:.3px;color:var(--white)}
.nav-sep{position:absolute;top:70px;font-size:18px;color:var(--white)}
.logo{position:absolute;font-family:"Cormorant Garamond",serif;font-weight:500;color:var(--gold);line-height:1}
.btn-outline{position:absolute;border:2px solid var(--gold);border-radius:30px;color:var(--gold);display:flex;align-items:center;justify-content:center;font-family:"Oswald",sans-serif;font-weight:300;font-size:20px;text-transform:uppercase}
.hero-title{position:absolute;left:86px;top:244px;width:600px;font-size:47px;line-height:52px;letter-spacing:.5px}
.hero-copy{position:absolute;left:86px;top:422px;width:505px;font-size:21px;line-height:31px;font-weight:300}

/* magazines */
.section-title{position:absolute;font-family:"Cormorant Garamond",serif;font-weight:400;font-size:48px;letter-spacing:.5px;line-height:1.1;color:var(--plum-deep)}
.section-sub{position:absolute;left:86px;top:896px;font-size:20px;font-weight:300;color:var(--grey)}
.cover{position:absolute;width:235px;height:325px;box-shadow:0 6px 16px rgba(0,0,0,.18)}
.cover-head{position:absolute;left:0;top:18px;width:235px;display:flex;align-items:center;justify-content:space-between;padding:0 18px}
.cover-head .meta{font-family:"Oswald",sans-serif;font-weight:300;font-size:12px;text-transform:uppercase}
.cover-head .name{font-family:"Cormorant Garamond",serif;font-weight:500;font-size:46px;line-height:1}
.cover svg{position:absolute;left:0;top:0}
.issue{position:absolute;width:260px;text-align:center;padding:0 12px}
.issue h3{font-family:"Oswald",sans-serif;font-weight:400;font-size:21px;text-transform:uppercase;color:var(--ink)}
.issue p{margin-top:10px;font-size:16px;line-height:24px;font-weight:300;color:var(--grey)}
.btn-dl{position:absolute;width:131px;height:42px;border:1.5px solid var(--ink);border-radius:22px;display:flex;align-items:center;justify-content:center;font-family:"Oswald",sans-serif;font-weight:400;font-size:13px;text-transform:uppercase;color:var(--ink)}

/* newsletter */
.newsletter{position:absolute;left:0;top:2215px;width:1200px;height:472px;background:var(--lavender);overflow:hidden}
.news-title{position:absolute;left:300px;top:112px;width:600px;text-align:center;font-size:47px;line-height:54px;letter-spacing:.5px;color:var(--plum-deep)}
.email{position:absolute;left:388px;top:249px;width:264px;height:49px;background:var(--white);font-size:13px;color:#8d8590;padding-left:17px;display:flex;align-items:center}
.btn-sub{position:absolute;left:669px;top:249px;width:140px;height:49px;border-radius:26px;background:var(--plum);color:var(--white);font-family:"Oswald",sans-serif;font-size:20px;font-weight:400;display:flex;align-items:center;justify-content:center}
.privacy{position:absolute;left:400px;top:333px;width:400px;text-align:center;font-size:15px;color:#4d4550}

/* about */
.about-copy{position:absolute;left:550px;top:2908px;width:530px;font-size:17.5px;line-height:25.5px;font-weight:300;color:var(--ink)}
.role{position:absolute;left:550px;font-size:18px;font-weight:300;color:var(--ink)}
.role b{font-weight:500}

/* footer */
.footer{position:absolute;left:0;top:3385px;width:1200px;height:360px;background:var(--plum);color:var(--white)}
.foot-head{position:absolute;top:72px;font-size:24px;font-family:"Cormorant Garamond",serif;font-weight:400}
.foot-text{position:absolute;left:86px;top:127px;width:340px;font-size:15px;line-height:23px;font-weight:300}
.foot-link{position:absolute;font-size:15.5px;font-weight:300}
.foot-social{text-decoration:underline}
</style>
</head>
<body>

<header class="hero">
  <span class="nav-link cond" style="left:86px">Home</span>
  <span class="nav-sep" style="left:140px">|</span>
  <span class="nav-link cond" style="left:165px">About us</span>
  <span class="nav-sep" style="left:242px">|</span>
  <span class="nav-link cond" style="left:268px">Submissions</span>

  <div class="logo" style="left:490px;top:20px;font-size:108px;width:220px;text-align:center">quirk</div>

  <span class="nav-link cond" style="left:778px">Purchase</span>
  <span class="nav-sep" style="left:855px">|</span>
  <span class="nav-link cond" style="left:881px">Contact</span>
  <div class="btn-outline" style="left:975px;top:55px;width:139px;height:54px">Subscribe</div>

  <h1 class="hero-title serif">Quirk is a plucky little pubication out of Wellington, New Zealand</h1>
  <p class="hero-copy">Quirk is a literary and arts journal that provides a platform for both emerging and established writers and artists from New Zealand and beyond</p>
  <div class="btn-outline" style="left:86px;top:547px;width:138px;height:51px">Donate us</div>

  <svg class="abs" style="left:0;top:0" width="1200" height="721" role="img" aria-label="Duotone pink photograph of a corridor of receding arches with steps">
    <defs><linearGradient id="arch" x1="0" y1="0" x2="0" y2="1"><stop offset="0" stop-color="#c9426f"/><stop offset="1" stop-color="#e0577f"/></linearGradient></defs>
    <path d="M748 612 V262 H770 V221 H1077 V262 H1098 V612 Z" fill="url(#arch)"/>
  </svg>
  <svg class="abs" style="left:0;top:0" width="1200" height="721" aria-hidden="true">
    <path d="M732 631 V258 H752 V221 H1093 V258 H1113 V631 Z" fill="none" stroke="#b79a2b" stroke-width="1.3"/>
    <path d="M770 221 V204 H1077 V221" fill="none" stroke="#b79a2b" stroke-width="1.3"/>
    <rect x="744" y="218" width="13" height="13" fill="none" stroke="#b79a2b" stroke-width="1.3"/>
    <rect x="1088" y="218" width="13" height="13" fill="none" stroke="#b79a2b" stroke-width="1.3"/>
  </svg>
</header>

<main>
  <h2 class="section-title" style="left:86px;top:826px">Our Upcoming Magazine</h2>
  <p class="section-sub">Our back catalogue is available in digital format for a reduced price.</p>

  <!-- row 1 -->
  <div class="cover" style="left:86px;top:972px;background:var(--cream)">
    <div class="cover-head"><span class="meta" style="color:#6b7a2a">Issue 001</span><span class="name" style="color:#6b7a2a">quirk</span><span class="meta" style="color:#6b7a2a">Aug 2022</span></div>
    <svg width="235" height="325" role="img" aria-label="Olive duotone portrait photograph"><path d="M20 325 V122 H40 V100 H195 V122 H215 V325 Z" fill="#8d8a2d"/><path d="M12 325 V110 H28 V92 H207 V110 H223 V325" fill="none" stroke="#d8c277" stroke-width="1"/></svg>
  </div>
  <div class="cover" style="left:349px;top:972px;background:var(--rose)">
    <div class="cover-head"><span class="meta" style="color:#f3ebdc">Issue 002</span><span class="name" style="color:#f3ebdc">quirk</span><span class="meta" style="color:#f3ebdc">Sep 2022</span></div>
    <svg width="235" height="325" role="img" aria-label="Magenta duotone photograph of geometric building facade"><path d="M20 325 V122 H40 V100 H195 V122 H215 V325 Z" fill="#9b3a63"/><path d="M12 325 V110 H28 V92 H207 V110 H223 V325" fill="none" stroke="#e1a9ba" stroke-width="1"/></svg>
  </div>
  <div class="cover" style="left:614px;top:972px;background:var(--white)">
    <div class="cover-head"><span class="meta" style="color:#c4587a">Issue 003</span><span class="name" style="color:#c4587a">quirk</span><span class="meta" style="color:#c4587a">Oct 2022</span></div>
    <svg width="235" height="325" role="img" aria-label="Blue and green duotone photograph of a palm leaf"><defs><linearGradient id="c3" x1="0" y1="0" x2="1" y2="1"><stop offset="0" stop-color="#2e3b8f"/><stop offset="1" stop-color="#3f7a3a"/></linearGradient></defs><path d="M20 325 V122 H40 V100 H195 V122 H215 V325 Z" fill="url(#c3)"/><path d="M12 325 V110 H28 V92 H207 V110 H223 V325" fill="none" stroke="#d8c277" stroke-width="1"/></svg>
  </div>
  <div class="cover" style="left:877px;top:972px;background:var(--olive)">
    <div class="cover-head"><span class="meta" style="color:#f3ebdc">Issue 004</span><span class="name" style="color:#c9b23a">quirk</span><span class="meta" style="color:#f3ebdc">Nov 2022</span></div>
    <svg width="235" height="325" role="img" aria-label="Pink duotone portrait photograph"><path d="M20 325 V122 H40 V100 H195 V122 H215 V325 Z" fill="#e06db9"/><path d="M12 325 V110 H28 V92 H207 V110 H223 V325" fill="none" stroke="#c9b23a" stroke-width="1"/></svg>
  </div>

  <div class="issue" style="left:73px;top:1328px"><h3>Issue 001 — Aug 2022</h3><p>Lorem ipsum dolor sit amet, consectetur adipiscing elit. Aenean dapibus</p></div>
  <div class="issue" style="left:337px;top:1328px"><h3>Issue 002 — Sep 2022</h3><p>Lorem ipsum dolor sit amet, consectetur adipiscing elit. Aenean dapibus</p></div>
  <div class="issue" style="left:602px;top:1328px"><h3>Issue 003 — Oct 2022</h3><p>Lorem ipsum dolor sit amet, consectetur adipiscing elit. Aenean dapibus</p></div>
  <div class="issue" style="left:865px;top:1328px"><h3>Issue 004 — Nov 2022</h3><p>Lorem ipsum dolor sit amet, consectetur adipiscing elit. Aenean dapibus</p></div>
  <div class="btn-dl" style="left:138px;top:1465px">Download now</div>
  <div class="btn-dl" style="left:401px;top:1465px">Download now</div>
  <div class="btn-dl" style="left:666px;top:1465px">Download now</div>
  <div class="btn-dl" style="left:929px;top:1465px">Download now</div>

  <!-- row 2 -->
  <div class="cover" style="left:86px;top:1562px;background:var(--white)">
    <div class="cover-head"><span class="meta" style="color:#c4587a">Issue 005</span><span class="name" style="color:#c4587a">quirk</span><span class="meta" style="color:#c4587a">Dec 2022</span></div>
    <svg width="235" height="325" role="img" aria-label="Violet duotone photograph of a palm frond"><path d="M20 325 V122 H40 V100 H195 V122 H215 V325 Z" fill="#8a6cb4"/><path d="M12 325 V110 H28 V92 H207 V110 H223 V325" fill="none" stroke="#d8c277" stroke-width="1"/></svg>
  </div>
  <div class="cover" style="left:349px;top:1562px;background:var(--cream)">
    <div class="cover-head"><span class="meta" style="color:#6b7a2a">Issue 006</span><span class="name" style="color:#6b7a2a">quirk</span><span class="meta" style="color:#6b7a2a">Jan 2023</span></div>
    <svg width="235" height="325" role="img" aria-label="Orange and teal duotone photograph of hands"><defs><linearGradient id="c6" x1="0" y1="0" x2="1" y2="1"><stop offset="0" stop-color="#4f8aa0"/><stop offset=".55" stop-color="#d46a2e"/><stop offset="1" stop-color="#e8552c"/></linearGradient></defs><path d="M20 325 V122 H40 V100 H195 V122 H215 V325 Z" fill="url(#c6)"/><path d="M12 325 V110 H28 V92 H207 V110 H223 V325" fill="none" stroke="#d8c277" stroke-width="1"/></svg>
  </div>
  <div class="cover" style="left:614px;top:1562px;background:var(--olive)">
    <div class="cover-head"><span class="meta" style="color:#f3ebdc">Issue 007</span><span class="name" style="color:#c9b23a">quirk</span><span class="meta" style="color:#f3ebdc">Feb 2023</span></div>
    <svg width="235" height="325" role="img" aria-label="Rose duotone fashion photograph"><path d="M20 325 V122 H40 V100 H195 V122 H215 V325 Z" fill="#a65668"/><path d="M12 325 V110 H28 V92 H207 V110 H223 V325" fill="none" stroke="#c9b23a" stroke-width="1"/></svg>
  </div>
  <div class="cover" style="left:877px;top:1562px;background:var(--rose)">
    <div class="cover-head"><span class="meta" style="color:#f3ebdc">Issue 008</span><span class="name" style="color:#f3ebdc">quirk</span><span class="meta" style="color:#f3ebdc">Mar 2023</span></div>
    <svg width="235" height="325" role="img" aria-label="Brown duotone photograph of palm shadows"><path d="M20 325 V122 H40 V100 H195 V122 H215 V325 Z" fill="#8b5d52"/><path d="M12 325 V110 H28 V92 H207 V110 H223 V325" fill="none" stroke="#e1a9ba" stroke-width="1"/></svg>
  </div>

  <div class="issue" style="left:73px;top:1918px"><h3>Issue 005 — Dec 2022</h3><p>Lorem ipsum dolor sit amet, consectetur adipiscing elit. Aenean dapibus</p></div>
  <div class="issue" style="left:337px;top:1918px"><h3>Issue 006 — Jan 2023</h3><p>Lorem ipsum dolor sit amet, consectetur adipiscing elit. Aenean dapibus</p></div>
  <div class="issue" style="left:602px;top:1918px"><h3>Issue 007 — Feb 2023</h3><p>Lorem ipsum dolor sit amet, consectetur adipiscing elit. Aenean dapibus</p></div>
  <div class="issue" style="left:865px;top:1918px"><h3>Issue 008 — Mar 2023</h3><p>Lorem ipsum dolor sit amet, consectetur adipiscing elit. Aenean dapibus</p></div>
  <div class="btn-dl" style="left:138px;top:2054px">Download now</div>
  <div class="btn-dl" style="left:401px;top:2054px">Download now</div>
  <div class="btn-dl" style="left:666px;top:2054px">Download now</div>
  <div class="btn-dl" style="left:929px;top:2054px">Download now</div>

  <section class="newsletter">
    <svg class="abs" style="left:780px;top:0" width="420" height="472" role="img" aria-label="Photograph of pink lavender sprigs on a lilac and pale blue background">
      <defs><linearGradient id="flow" x1="0" y1="0" x2="1" y2="1"><stop offset="0" stop-color="#e6d6ef" stop-opacity="0"/><stop offset=".45" stop-color="#d79be2"/><stop offset=".8" stop-color="#c678d8"/><stop offset="1" stop-color="#a9d8ea"/></linearGradient></defs>
      <rect width="420" height="472" fill="url(#flow)"/>
    </svg>
    <h2 class="news-title serif">Subscribe to our weekly newsletter</h2>
    <div class="email">Email Address</div>
    <div class="btn-sub">SUBSCRIBE</div>
    <p class="privacy">We respect your privacy.</p>
  </section>

  <svg class="abs" style="left:0;top:2790px" width="500" height="490" role="img" aria-label="Plum duotone portrait photograph">
    <path d="M100 454 V62 H129 V33 H423 V62 H452 V454 Z" fill="#4d1f44"/>
  </svg>
  <svg class="abs" style="left:0;top:2790px" width="500" height="490" aria-hidden="true">
    <path d="M86 473 V40 H114 V14 H438 V40 H467 V473 Z" fill="none" stroke="#b79a2b" stroke-width="1.3"/>
    <rect x="96" y="34" width="13" height="13" fill="none" stroke="#b79a2b" stroke-width="1.3"/>
    <rect x="443" y="34" width="13" height="13" fill="none" stroke="#b79a2b" stroke-width="1.3"/>
  </svg>

  <h2 class="section-title" style="left:550px;top:2838px">About Quirk</h2>
  <p class="about-copy">QUIRK is an independent literary annual journal established in 2022 by Hazel Wintergate and Mereana Clift that publishes unrepentant unfiltered accounts of life, eclectic takes on the mundane ordinary, and deep dives into modern love &amp; sexuality.</p>
  <p class="role" style="top:3056px"><b>Founder, Editor</b>: Hazel Arohanui Wintergate</p>
  <p class="role" style="top:3101px"><b>Founder, Production Director</b>: Mereana Clift</p>
  <p class="role" style="top:3146px"><b>Art Direction</b>: Lorna Pike</p>
  <p class="role" style="top:3191px"><b>Editorial Assistant</b>: Kirsten Holloway-Dunn</p>
</main>

<footer class="footer">
  <h4 class="foot-head" style="left:86px">Support Us</h4>
  <p class="foot-text">Since our launch in 2022, we have relied upon the generous support of our creative business community in Wellington City, New Zealand. If you read us, or love our ethos, please consider a donation.</p>
  <div class="abs cond" style="left:86px;top:262px;font-size:20px;font-weight:400;display:flex;align-items:center;gap:12px">CHIP IN HERE
    <svg width="22" height="12" viewBox="0 0 22 12" aria-hidden="true"><path d="M0 6 H20 M15 1 L20 6 L15 11" fill="none" stroke="#fff" stroke-width="1.4"/></svg>
  </div>

  <h4 class="foot-head" style="left:560px">Main Menu</h4>
  <span class="foot-link" style="left:560px;top:127px">Home</span>
  <span class="foot-link" style="left:560px;top:165px">About</span>
  <span class="foot-link" style="left:560px;top:203px">Submissions</span>
  <span class="foot-link" style="left:560px;top:241px">Purchase</span>
  <span class="foot-link" style="left:560px;top:279px">Contact</span>

  <h4 class="foot-head" style="left:775px">Social</h4>
  <span class="foot-link foot-social" style="left:776px;top:127px">Facefolio</span>
  <span class="foot-link foot-social" style="left:776px;top:165px">Snapgram</span>
  <span class="foot-link foot-social" style="left:776px;top:203px">Chirper</span>

  <div class="logo" style="left:954px;top:60px;font-size:84px;width:170px;text-align:center">quirk</div>
  <p class="foot-link" style="left:942px;top:178px">Made with <span style="color:var(--gold);text-decoration:underline">Sitecraft</span></p>
</footer>

</body>
</html>
```